Ferncrest Dental, LLC business card project

Business card to be designed with current logo.
Dental office- please keep design of card that looks clean and professional.
Please include the following info:
Ferncrest Dental, LLC
Dr. Lorna Pettigrew
2871 Marlowe Street
Bethlehem, PA 18093
610-555-0193
ferncrestdental.office@examplemail.test
Hello everyone-
Reason: Just got back from overseas- will look at all designs and provide feedback. Thank you!
Reason: Polling my friends for the final selection-
thank you to all those that participated- so many talented designers!

```html
<!DOCTYPE html>
<html lang="en">
<head>
<meta charset="utf-8">
<title>Ferncrest Dental — Business Card</title>
<link rel="stylesheet" href="https://fonts.googleapis.com/css2?family=Tinos:ital@0;1&display=swap">
<style>
  :root {
    --page-bg: #f3f3f3;
    --card-green: #5e9a3e;
    --card-edge: #c9dc8f;
    --card-shadow: rgba(40, 40, 40, 0.85);
    --logo-bg: #ffffff;
    --logo-ink: #7aa83a;
    --text-light: #f4f7ee;
  }
  html, body {
    margin: 0;
    padding: 0;
    overflow: hidden;
  }
  body {
    width: 1200px;
    height: 900px;
    background: var(--page-bg);
    position: relative;
    font-family: "Tinos", "Times New Roman", serif;
  }
  .business-card {
    position: absolute;
    left: 316px;
    top: 56px;
    width: 424px;
    height: 534px;
    box-sizing: border-box;
    background: var(--card-green);
    border: 2px solid var(--card-edge);
    box-shadow: 10px 12px 8px var(--card-shadow);
  }
  .logo-plate {
    position: absolute;
    left: 123px;
    top: 8px;
    width: 288px;
    height: 98px;
    background: var(--logo-bg);
    box-shadow: 6px 8px 6px var(--card-shadow);
    display: flex;
    align-items: center;
    justify-content: center;
    gap: 10px;
  }
  .logo-mark {
    width: 16px;
    height: 16px;
    border-radius: 50%;
    background: var(--logo-ink);
  }
  .logo-name {
    font-size: 31px;
    font-weight: 400;
    color: var(--logo-ink);
    letter-spacing: -0.3px;
  }
  .contact-block {
    position: absolute;
    left: 0;
    right: 0;
    top: 343px;
    margin: 0;
    text-align: center;
    font-style: italic;
    font-size: 20px;
    line-height: 32.3px;
    color: var(--text-light);
  }
  .contact-block span {
    display: block;
  }
</style>
</head>
<body>
  <div class="business-card">
    <div class="logo-plate">
      <span class="logo-mark"></span>
      <span class="logo-name">Ferncrest Dental</span>
    </div>
    <address class="contact-block">
      <span class="doctor-name">Dr. Lorna Pettigrew</span>
      <span class="street">2871 Marlowe Street</span>
      <span class="city">Bethlehem, PA 18093</span>
      <span class="phone">610-555-0193</span>
      <span class="email">ferncrestdental.office@examplemail.test</span>
    </address>
  </div>
</body>
</html>
```